New business card for Building services company

I own a small 1 person business which primarily works at heights. I gain access to my work areas via ladders and use safety harnesses. I conduct gutter cleaning, roof cleaning with a pressure cleaner(water blaster), ground level pressure cleaning (driveways, footpaths and walls), I also do small handy-man jobs & gardening/ tree trimming.

I have just had a logo designed by Sketch Hive, which I will upload. I'd like to see the themes followed through.
I like the colour of aqua or the colours what is in the logo.

I live in tropical north Queensland in Cairns, Australia. It is where the rain forest meets the Coral Lantern Shoal. On average it is 30+ degrees C.
Updates

Hello all designers. Thankyou for all the submissions so far. The following are my business details which I need on the card-

VERNO Roof, Gutter & Pressure Cleaning Services.
Director -Dale Marwick
Ph 0417385026
Email- roofcleaning@plovernet.example.au
ABN -48 902 317 254

Please include the following services which my business conducts-
*Gutter Cleaning
*Pressure Cleaning- Roof's, Driveways etc
*Minor Roof, Gutter & Building Maintenance
*Garden waste removal & complex cleanups

Public Liability upto $10 Million
Working at Heights Cert.

Quote-                                     Date-

Hi everyone,  could you please ensure you have -"Quote" and "Date" on the card. I'll need space to hand write details on the card for the specific details.        

Requirements
Must have
• The logo attached must be included.
• The rear side of the card is dedicated to job quoted and price of the job.
• *Please include- Quote price, Quote date. etc
• Including the tasks I do at work around the side of the card- Gutter Cleaning; Roof Cleaning, Gutter Maintenance; Gardening; Pressure Cleaning Roof's, Driveways etc.
Nice to have
• The rear side to have a ladder

```html
<!DOCTYPE html>
<html lang="en">
<head>
<meta charset="utf-8">
<title>VERNO Business Card – Front</title>
<link rel="stylesheet" href="https://fonts.googleapis.com/css2?family=Cinzel:wght@400;700&display=swap">
<style>
  :root {
    --page-bg: #ffffff;
    --label-ink: #000000;
    --green-deep: #056b3a;
    --green: #0a9447;
    --sheen: #f3f5e0;
    --aqua-soft: #7fcfb0;
    --aqua: #00aa9c;
    --blue: #1c75bc;
    --blue-mid: #2a4ca0;
    --navy: #2b3990;
    --wordmark: #2e3f9e;
    --tagline: #f4ecd0;
    --phone: #43b8a8;
  }
  html, body {
    margin: 0;
    padding: 0;
    width: 1200px;
    height: 673px;
    overflow: hidden;
    background: var(--page-bg);
  }
  .sheet {
    position: relative;
    width: 1200px;
    height: 673px;
  }
  .side-label {
    position: absolute;
    left: 58px;
    top: 84px;
    width: 64px;
    margin: 0;
    font-family: "Cinzel", serif;
    font-weight: 400;
    font-size: 84px;
    line-height: 88px;
    color: var(--label-ink);
    text-align: center;
  }
  .side-label span { display: block; }
  .card {
    position: absolute;
    left: 174px;
    top: 38px;
    width: 997px;
    height: 599px;
  }
  .card svg { display: block; }
  .wordmark {
    font-family: "Cinzel", serif;
    font-weight: 700;
    fill: var(--wordmark);
  }
  .tagline {
    font-family: "Cinzel", serif;
    font-weight: 400;
    fill: var(--tagline);
  }
  .phone {
    font-family: "Cinzel", serif;
    font-weight: 400;
    fill: var(--phone);
  }
</style>
</head>
<body>
<main class="sheet">
  <p class="side-label" aria-label="Front">
    <span>F</span><span>R</span><span>O</span><span>N</span><span>T</span>
  </p>

  <section class="card" aria-label="VERNO business card front">
    <svg width="997" height="599" viewBox="0 0 997 599">
      <defs>
        <linearGradient id="card-fill" x1="0" y1="0" x2="0" y2="1">
          <stop offset="0" stop-color="var(--green-deep)"/>
          <stop offset="0.10" stop-color="var(--green)"/>
          <stop offset="0.155" stop-color="var(--sheen)"/>
          <stop offset="0.18" stop-color="var(--sheen)"/>
          <stop offset="0.22" stop-color="var(--aqua-soft)"/>
          <stop offset="0.28" stop-color="var(--aqua)"/>
          <stop offset="0.50" stop-color="var(--aqua)"/>
          <stop offset="0.64" stop-color="var(--blue)"/>
          <stop offset="0.86" stop-color="var(--blue-mid)"/>
          <stop offset="1" stop-color="var(--navy)"/>
        </linearGradient>
      </defs>

      <rect class="card-face" x="0" y="0" width="997" height="599" fill="url(#card-fill)"/>

      <text class="wordmark" x="498" y="407" font-size="210" text-anchor="middle"
            textLength="800" lengthAdjust="spacingAndGlyphs">VERNO</text>

      <text class="tagline" x="498" y="460" font-size="31" text-anchor="middle"
            textLength="895" lengthAdjust="spacingAndGlyphs">ROOF, GUTTER &amp; PRESSURE CLEANING SERVECES</text>

      <text class="phone" x="499" y="552" font-size="50" text-anchor="middle"
            textLength="437" lengthAdjust="spacingAndGlyphs">C<tspan font-size="36">ALL</tspan>  0417 385 026</text>
    </svg>
  </section>
</main>
</body>
</html>
```